Stationery Design Project for Velmoran Tisk

This project is linked to Corporate Identity of VelmoranTisk.

Our company needs a Stationery Design. Please refer to our original project in the link above.

Stationary
Once The Logo, Look & feel with colour palette and Typography has been set, develop a stationary with the following items:
• Business Card
• Letter A4
• A5 Card
Suggest 3 of each.

Industry/Entity Type

Business

Font styles to use
Other font styles liked:
• Calibri, Arial, Myriad, Helvetica Neue, Lucida Grande, Avenir

```html
<!DOCTYPE html>
<html lang="en">
<head>
<meta charset="utf-8">
<title>Velmoran Tisk — Letterhead A4</title>
<link rel="stylesheet" href="https://fonts.googleapis.com/css2?family=Josefin+Sans:wght@300&family=Lato:wght@400&display=swap">
<style>
  :root {
    --backdrop: #ececec;
    --paper: #fbfbfa;
    --taupe: #6e6158;
    --sand: #c8b39a;
    --ink: #5a534e;
  }
  html, body {
    margin: 0;
    width: 1200px;
    height: 795px;
    overflow: hidden;
    background: var(--backdrop);
  }
  .letterhead {
    position: absolute;
    left: 340px;
    top: 30px;
    width: 520px;
    height: 735px;
    background: var(--paper);
    box-shadow: 0 2px 10px rgba(0,0,0,0.12);
    overflow: hidden;
  }
  .letterhead__waves {
    position: absolute;
    inset: 0;
    width: 100%;
    height: 100%;
  }
  .wave--taupe { fill: var(--taupe); }
  .wave--sand { fill: var(--sand); }
  .brand {
    position: absolute;
    top: 88px;
    left: 0;
    right: 0;
    text-align: center;
    color: var(--ink);
  }
  .brand__name {
    display: inline-flex;
    align-items: center;
    gap: 14px;
    margin: 0;
    font-family: "Josefin Sans", sans-serif;
    font-weight: 300;
    font-size: 22px;
    letter-spacing: 0.28em;
    text-transform: uppercase;
    color: var(--ink);
  }
  .brand__dot {
    width: 7px;
    height: 7px;
    border-radius: 50%;
    background: var(--ink);
  }
  .brand__contact {
    margin: 10px 0 0;
    font-family: "Lato", sans-serif;
    font-size: 6.5px;
    line-height: 1.6;
    letter-spacing: 0.04em;
    color: var(--ink);
  }
</style>
</head>
<body>
  <main class="letterhead">
    <svg class="letterhead__waves" viewBox="0 0 520 735" aria-hidden="true">
      <g class="wave wave--top-left">
        <path class="wave--sand" d="M0 0 H228 C202 40 130 44 82 80 C36 114 18 190 0 352 Z"/>
        <path class="wave--taupe" d="M0 0 H215 C190 30 120 36 70 70 C26 104 10 182 0 340 Z"/>
      </g>
      <g class="wave wave--bottom-right" transform="rotate(180 260 367.5)">
        <path class="wave--sand" d="M0 0 H262 C232 52 150 60 92 100 C40 140 18 230 0 392 Z"/>
        <path class="wave--taupe" d="M0 0 H248 C220 40 140 50 80 90 C28 128 10 220 0 380 Z"/>
      </g>
    </svg>

    <header class="brand">
      <h1 class="brand__name">Velmoran <span class="brand__dot"></span> Tisk</h1>
      <p class="brand__contact">
        27 Linden Row, Brookfield State<br>
        40210 Country<br>
        T: 555 010 2234 &nbsp;|&nbsp; F: 555 010 2235<br>
        E: hello@velmorantisk.com &nbsp;|&nbsp; W: www.velmorantisk.com
      </p>
    </header>
  </main>
</body>
</html>
```